Business card design needed

I need a business card design for a dog walking, dog minding and dog training business. Please refer to my website for the basic company colours and fonts I'm after. Planning on a double sided card, so all information doesn't need to be on the 'front' side.
Cheers

Industry/Entity Type

Dog Training

Contact Information for Business Card

Meadow Paws - happy hounds
Rua 0498307164
meadowpawsdemo.com.au
-walking
-holiday stays
-onsite care
-training and behavioural consultations

```html
<!DOCTYPE html>
<html lang="en">
<head>
<meta charset="utf-8">
<title>Meadow Paws – Business Card</title>
<link href="https://fonts.googleapis.com/css2?family=Jost:wght@400;500&family=Arimo&family=Pinyon+Script&display=swap" rel="stylesheet">
<style>
  :root {
    --page: #ffffff;
    --silver-light: #f4f4f5;
    --silver-mid: #d3d4d6;
    --silver-dark: #a9abae;
    --charcoal: #2c2b2a;
    --charcoal-deep: #1c1917;
    --brand-orange: #d9501e;
    --brand-grey: #666769;
    --ink: #1a1a1a;
    --card-text: #f2f2f2;
  }
  html, body {
    margin: 0;
    padding: 0;
    width: 1200px;
    height: 956px;
    overflow: hidden;
    background: var(--page);
  }
  .canvas {
    position: relative;
    width: 1200px;
    height: 956px;
  }
  .card {
    position: absolute;
    top: 170px;
    width: 376px;
    height: 615px;
    border-radius: 22px;
    box-shadow: 0 2px 6px rgba(0,0,0,0.18);
    overflow: hidden;
  }
  .card--front {
    left: 212px;
    background: radial-gradient(ellipse at 50% 52%, var(--silver-light) 0%, var(--silver-mid) 55%, var(--silver-dark) 100%);
  }
  .card--back {
    left: 612px;
    background: linear-gradient(135deg, var(--charcoal) 0%, var(--charcoal-deep) 100%);
    color: var(--card-text);
  }
  .brand-mark {
    position: absolute;
    left: 50%;
    transform: translateX(-50%);
    border-radius: 50%;
    box-sizing: border-box;
  }
  .card--front .brand-mark {
    top: 130px;
    width: 192px;
    height: 192px;
    background: var(--charcoal-deep);
    border: 6px solid var(--brand-orange);
  }
  .card--back .brand-mark {
    top: 102px;
    width: 104px;
    height: 104px;
    background: var(--charcoal-deep);
    border: 3px solid var(--brand-orange);
  }
  .brand-name {
    position: absolute;
    top: 338px;
    left: 0;
    right: 0;
    margin: 0;
    text-align: center;
    font-family: "Jost", sans-serif;
    font-weight: 500;
    font-size: 40px;
    letter-spacing: 1px;
    color: var(--brand-grey);
    white-space: nowrap;
  }
  .tagline {
    position: absolute;
    top: 466px;
    left: 0;
    right: 0;
    margin: 0;
    text-align: center;
    font-family: "Arimo", sans-serif;
    font-size: 17px;
    color: var(--ink);
  }
  .services {
    position: absolute;
    top: 232px;
    left: 0;
    right: 0;
    margin: 0;
    padding: 0;
    list-style: none;
    text-align: center;
    font-family: "Jost", sans-serif;
    font-variant: small-caps;
    font-size: 15px;
    line-height: 17px;
    letter-spacing: 1.6px;
    white-space: nowrap;
  }
  .contact-name {
    position: absolute;
    top: 440px;
    left: 56px;
    margin: 0;
    font-family: "Pinyon Script", cursive;
    font-size: 34px;
    font-weight: 400;
  }
  .contact-line {
    position: absolute;
    left: 60px;
    display: flex;
    align-items: center;
    gap: 6px;
    font-family: "Jost", sans-serif;
    font-size: 18px;
    line-height: 22px;
    letter-spacing: 0.2px;
    white-space: nowrap;
  }
  .contact-line--phone { top: 500px; }
  .contact-line--web { top: 530px; }
  .contact-icon {
    flex: none;
    width: 12px;
    display: flex;
    justify-content: center;
  }
</style>
</head>
<body>
<main class="canvas">
  <section class="card card--front" aria-label="Card front">
    <div class="brand-mark" aria-hidden="true"></div>
    <h1 class="brand-name">MEADOW PAWS</h1>
    <p class="tagline">happy hounds</p>
  </section>

  <section class="card card--back" aria-label="Card back">
    <div class="brand-mark" aria-hidden="true"></div>
    <ul class="services">
      <li>Walking</li>
      <li>Holiday stays</li>
      <li>Onsite care</li>
      <li>Training</li>
      <li>&amp;</li>
      <li>Behavioural Consultations</li>
    </ul>
    <h2 class="contact-name">Rua</h2>
    <div class="contact-line contact-line--phone">
      <span class="contact-icon">
        <svg width="10" height="18" viewBox="0 0 10 18" aria-hidden="true">
          <rect x="0.5" y="0.5" width="9" height="17" rx="1.5" fill="none" stroke="currentColor"/>
          <rect x="2" y="2.5" width="6" height="5" fill="currentColor"/>
          <rect x="2" y="10" width="6" height="5" fill="currentColor" opacity="0.6"/>
        </svg>
      </span>
      <span>: 049-830-7164</span>
    </div>
    <div class="contact-line contact-line--web">
      <span class="contact-icon">
        <svg width="12" height="12" viewBox="0 0 12 12" aria-hidden="true">
          <rect width="12" height="12" fill="currentColor"/>
        </svg>
      </span>
      <span>: www.meadowpawsdemo.com.au</span>
    </div>
  </section>
</main>
</body>
</html>
```